Inspiration Poster

Inspirational Poster that has a Kamran Dulo like abstract look (http://www.vexalo.com/images/search?q=kamran+dulo&FORM=HDRSC2) with the text:

"we walk not in order to arrive at the promise land but because walking itself is a revolution"
-Peter Ambrick

```html
<!DOCTYPE html>
<html lang="en">
<head>
<meta charset="utf-8">
<title>Inspiration Poster – Walking Is a Revolution</title>
<link rel="stylesheet" href="https://fonts.googleapis.com/css2?family=Source+Sans+3:wght@400&display=swap">
<style>
  :root {
    --paper: #ffffff;
    --ink: #111111;
    --mint: #eefcf6;
    --aqua: #8df2da;
    --cyan: #45d8e4;
    --sky: #33a6e6;
    --deep-blue: #2c5ce0;
  }
  html, body {
    margin: 0;
    padding: 0;
    overflow: hidden;
    background: var(--paper);
  }
  .poster {
    position: relative;
    width: 871px;
    height: 1200px;
    background: var(--paper);
    overflow: hidden;
    font-family: "Source Sans 3", "Myriad Pro", Arial, sans-serif;
    color: var(--ink);
  }
  .poster__sweep {
    position: absolute;
    inset: 0;
    width: 871px;
    height: 1200px;
  }
  .poster__quote {
    position: absolute;
    left: 47px;
    top: 100px;
    margin: 0;
    font-size: 48px;
    font-weight: 400;
    line-height: 60px;
    letter-spacing: -0.4px;
    white-space: nowrap;
  }
  .poster__quote span { display: block; }
  .poster__author {
    position: absolute;
    left: 37px;
    top: 556px;
    margin: 0;
    font-size: 80px;
    font-weight: 400;
    line-height: 1;
    letter-spacing: -1px;
    white-space: nowrap;
  }
</style>
</head>
<body>
  <main class="poster">
    <svg class="poster__sweep" viewBox="0 0 871 1200" role="img" aria-label="Abstract brushed sweep in aqua and blue tones curving from the lower left corner up to the top right">
      <defs>
        <linearGradient id="sweep-tone" x1="0.2" y1="0.1" x2="0.9" y2="1">
          <stop offset="0" stop-color="var(--mint)"/>
          <stop offset="0.35" stop-color="var(--aqua)"/>
          <stop offset="0.6" stop-color="var(--cyan)"/>
          <stop offset="0.82" stop-color="var(--sky)"/>
          <stop offset="1" stop-color="var(--deep-blue)"/>
        </linearGradient>
      </defs>
      <path class="sweep__area" d="M871 40 C840 560 520 920 0 1160 L0 1200 L871 1200 Z" fill="url(#sweep-tone)"/>
    </svg>

    <p class="poster__quote">
      <span>"We walk not in order</span>
      <span>to arrive at&nbsp; the promise land</span>
      <span>but because walking itself is a revolution"</span>
    </p>

    <p class="poster__author">-Peter Ambrick</p>
  </main>
</body>
</html>
```